Kiddies Tinker Harbour

We are a company that is going to offer birthday party hire of construction toys for boys to learn to develop their skills, e.g.: brikko, blocks, building supplies etc. We are also in the process of setting up an onsite location for birthday parties, where the kids can be entertained by the equipment and the parents can have a coffee and relax during the week and birthday parties during the weekend. We do require a booking system where people can book - it needs to take the booking and then we will email them out a confirmation with payment details on it and they can pay directly into our bank account.

Industry/Entity Type

Construction

Number of Pages Required

5+ page

Font styles to use
Sans Serif

Requirements
Should not have
• No mention of Brikko brand, use building bricks instead

```html
<!DOCTYPE html>
<html lang="en">
<head>
<meta charset="utf-8">
<title>Kiddies Tinker Harbour</title>
<link href="https://fonts.googleapis.com/css2?family=Roboto:wght@400;500;700;900&display=swap" rel="stylesheet">
<style>
:root{
  --dark:#161616;--blue:#2a86c6;--sky:#c3e9f9;--sky-light:#dff3fc;
  --green:#a3c13c;--red:#d9291d;--yellow:#f5c518;--grey-btn:#5f5f5f;
  --text:#555;--panel:#efefef;--white:#fff;
}
*{box-sizing:border-box;margin:0;padding:0}
html,body{width:756px;height:1200px;overflow:hidden}
body{font-family:'Roboto',sans-serif;background:var(--white);position:relative;color:var(--text)}
.abs{position:absolute}
.stripe{position:absolute;left:0;width:756px;height:2px;
  background:linear-gradient(90deg,var(--blue) 0 16%,var(--green) 16% 33%,var(--red) 33% 50%,var(--yellow) 50% 66%,var(--green) 66% 83%,var(--blue) 83%)}
.site-header{left:0;top:0;width:756px;height:82px;background:var(--dark)}
.brand{display:flex;align-items:center;gap:6px;color:var(--white);font-weight:700;font-size:14px;line-height:1.1}
.brand .dot{width:12px;height:12px;background:var(--yellow);border-radius:50%}
.call-label{left:426px;top:27px;color:var(--white);font-size:12px;font-weight:500}
.call-number{left:426px;top:38px;color:var(--yellow);font-size:20px;font-weight:700;letter-spacing:.5px}
.social{left:578px;top:34px;display:flex;gap:5px}
.social span{width:19px;height:19px;border-radius:50%;background:#3a3a3a;border:1px solid #777}
.hero-bg{left:0;top:82px;width:756px;height:330px;background:linear-gradient(180deg,var(--sky) 0%,var(--sky-light) 70%,#fff 100%)}
.hero-photo{left:47px;top:82px;width:662px;height:320px;border:2px solid #fff;border-top:0;
  border-radius:0 0 50% 50%/0 0 46px 46px;background:linear-gradient(180deg,#b9bcc4 0%,#d4d3d3 60%,#c8c5c2 100%);
  box-shadow:0 18px 14px -10px rgba(0,0,0,.25)}
.hero-arrows{left:356px;top:361px;display:flex;gap:4px}
.hero-arrows span{width:18px;height:18px;border-radius:50%;background:#eee;border:1px solid #999;display:flex;align-items:center;justify-content:center}
.booking{left:468px;top:116px;width:203px;height:226px;background:#fff;border-radius:5px;box-shadow:0 2px 6px rgba(0,0,0,.3);overflow:hidden}
.booking h2{height:30px;background:linear-gradient(#3d9ad8,#2076b8);color:#fff;font-size:17px;font-weight:500;text-align:center;line-height:30px}
.booking .field{margin:4px 9px 0;height:29px;border:1px solid #ccc;font-size:9px;color:#555;text-align:center;line-height:27px}
.booking .field:first-of-type{margin-top:8px}
.booking .field.msg{height:47px;line-height:22px}
.booking .book{margin:4px 9px 0;height:28px;background:var(--red);color:#fff;font-size:13px;font-weight:500;text-align:center;line-height:28px}
.title{color:var(--blue);font-size:17px;font-weight:500}
.welcome-title{left:0;top:438px;width:756px;text-align:center}
.welcome-text{left:54px;top:471px;width:648px;text-align:center;font-size:8.4px;line-height:16px}
.btn{display:block;height:27px;background:var(--grey-btn);color:#fff;font-size:8.5px;font-weight:500;text-align:center;line-height:27px;letter-spacing:.3px}
.what-do{left:47px;top:593px;width:208px;height:222px;background:var(--green);padding:15px 13px}
.what-do h3{color:#fff;font-size:16px;font-weight:500}
.what-do .photo{margin-top:9px;height:82px;background:linear-gradient(135deg,#9a8f84,#c9b05a 50%,#6f7fa0)}
.what-do p{margin-top:12px;color:#eef5d8;font-size:8.2px;line-height:14.5px}
.what-do .btn{margin-top:10px;width:95px}
.offers{left:273px;top:593px;width:436px;height:222px;background:var(--panel);padding:15px 13px;box-shadow:0 6px 6px -4px rgba(0,0,0,.2)}
.offers .title{font-size:16px}
.offer-list{display:flex;gap:8px;margin-top:10px;margin-left:5px}
.offer{width:130px}
.offer .photo{height:98px;border:3px solid}
.offer h4{margin-top:13px;font-size:10px;font-weight:500}
.offer p{margin-top:3px;font-size:8.4px;line-height:14.5px;padding-right:6px}
.onsite{left:0;top:844px;width:756px;height:212px;background:var(--sky)}
.onsite-photo{left:47px;top:868px;width:266px;height:164px;background:linear-gradient(135deg,#dfe6e8,#c7b79b 55%,#9b8a6c)}
.onsite-title{left:330px;top:866px}
.onsite-text{left:330px;top:892px;width:380px;font-size:8.4px;line-height:16px}
.site-footer{left:0;top:1056px;width:756px;height:144px;background:var(--dark)}
.footer-small{font-size:7.5px;color:#aaa;line-height:15.5px}
.f-head{font-size:10.5px;color:var(--blue);font-weight:500}
.links{font-size:8px;color:#ccc;line-height:13.5px;margin-top:3px}
.contact-name{font-size:7.8px;color:var(--blue);font-weight:500;margin-top:3px}
.contact-line{font-size:7.8px;color:#ccc;line-height:13.5px}
.contact-line.accent{color:#e8b420;display:flex;align-items:center;gap:3px}
.map{left:514px;top:1078px;width:195px;height:100px;background:linear-gradient(135deg,#e8e4d8,#cfe1c4 50%,#e9dfc5)}
</style>
</head>
<body>
<div class="abs hero-bg"></div>

<header class="abs site-header">
  <div class="brand abs" style="left:47px;top:24px">
    <span class="dot"></span><span>Kiddies<br>Tinker Harbour</span>
  </div>
  <div class="abs call-label">CALL US TODAY:</div>
  <div class="abs call-number">555-014-2287</div>
  <div class="abs social" aria-label="Social links"><span></span><span></span><span></span><span></span><span></span><span></span></div>
</header>
<div class="stripe" style="top:0"></div>

<div class="abs hero-photo" role="img" aria-label="Two toddlers building a tall tower from colourful building bricks"></div>
<div class="abs hero-arrows">
  <span><svg width="8" height="8" viewBox="0 0 8 8"><path d="M5.5 1 2.5 4l3 3" stroke="#555" stroke-width="1.5" fill="none"/></svg></span>
  <span><svg width="8" height="8" viewBox="0 0 8 8"><path d="M2.5 1l3 3-3 3" stroke="#555" stroke-width="1.5" fill="none"/></svg></span>
</div>

<form class="abs booking">
  <h2>QUICK BOOKING</h2>
  <div class="field">Full Name</div>
  <div class="field">Email Address</div>
  <div class="field">Contact No</div>
  <div class="field msg">Type Message</div>
  <div class="book">BOOK NOW</div>
</form>

<h1 class="abs title welcome-title">WELCOME TO OUR WEBSITE</h1>
<p class="abs welcome-text">Aliquam molestie, mi et imperdiet euismod, dui purus auctor tellus, et interdum lacus lectus et ante. Sed accumsan sollicitudin sapien, sit amet adipiscing turpis gravida ac. In congue, neque ac lobortis volutpat, libero mauris varius mi, vitae suscipit ipsum ligula vitae risus. Duis aliquam nibh a dui iaculis viverra id a velit. Vivamus egestas risus in magna varius commodo. Sed semper viverra egestas. Etiam pretium porttitor lectus, vel ornare neque porta volutpat.</p>
<a class="abs btn" style="left:330px;top:537px;width:96px">READ MORE</a>

<section class="abs what-do">
  <h3>WHAT WE DO</h3>
  <div class="photo" role="img" aria-label="Play table filled with trays of building bricks"></div>
  <p>Duis aliquam nibh a dui iaculis viverra id a velit. Vivamus egestas risus in magna varius commodo. Sed semper viverra egestas.</p>
  <a class="btn">READ MORE</a>
</section>

<section class="abs offers">
  <h3 class="title">WHAT WE OFFERS</h3>
  <div class="offer-list">
    <div class="offer">
      <div class="photo" style="border-color:var(--red);background:linear-gradient(135deg,#7fc6e6,#e85aa0 55%,#f2c230)" role="img" aria-label="Hands stacking colourful bricks"></div>
      <h4 style="color:var(--red)">BUILDING BRICKS</h4>
      <p>Duis aliquam nibh a dui iaculis viverra id a velit. Vivamus egestas risus in magna</p>
    </div>
    <div class="offer">
      <div class="photo" style="border-color:#3f9a2c;background:linear-gradient(135deg,#e0c23a,#4a8fd0 50%,#d64534)" role="img" aria-label="Toddler playing among large building blocks"></div>
      <h4 style="color:#3f9a2c">BLOCKS</h4>
      <p>Duis aliquam nibh a dui iaculis viverra id a velit. Vivamus egestas risus in magna</p>
    </div>
    <div class="offer">
      <div class="photo" style="border-color:var(--blue);background:linear-gradient(135deg,#f2f2f2,#e6c640 45%,#d23a2a 70%,#eeeeee)" role="img" aria-label="Toy construction site with a digger and figures"></div>
      <h4 style="color:var(--blue)">BUILDING SUPPLIES</h4>
      <p>Duis aliquam nibh a dui iaculis viverra id a velit. Vivamus egestas risus in magna</p>
    </div>
  </div>
</section>

<section class="abs onsite"></section>
<div class="stripe" style="top:844px"></div>
<div class="abs onsite-photo" role="img" aria-label="Two children building with bricks at a garden table"></div>
<h2 class="abs title onsite-title">ONSITE LOCATION</h2>
<p class="abs onsite-text">Aliquam molestie, mi et imperdiet euismod, dui purus auctor tellus, et interdum lacus lectus et ante. Sed accumsan sollicitudin sapien, sit amet adipiscing turpis gravida ac. In congue, neque ac lobortis volutpat, libero mauris varius mi, vitae suscipit ipsum ligula vitae risus. Duis aliquam nibh a dui iaculis viverra id a velit. Vivamus egestas risus in magna varius commodo. Sed semper viverra egestas. Etiam pretium porttitor lectus, vel ornare neque porta volutpat.</p>
<a class="abs btn" style="left:330px;top:992px;width:96px">READ MORE</a>

<footer class="abs site-footer">
  <div class="brand abs" style="left:47px;top:42px;font-size:12px">
    <span class="dot"></span><span>Kiddies<br>Tinker Harbour</span>
  </div>
  <div class="abs footer-small" style="left:47px;top:78px">Copyright ©2015. All Right Reserved.<br>Terms of Services</div>
  <div class="abs" style="left:229px;top:22px">
    <div class="f-head">COMPANY</div>
    <div class="links">Home<br>Who We Are<br>What We Do<br>Photo Gallery<br>News &amp; Events<br>Contact Us</div>
  </div>
  <div class="abs" style="left:352px;top:22px">
    <div class="f-head">CONTACT ADDRESS</div>
    <div class="contact-name">KIDDIES TINKER HARBOUR</div>
    <div class="contact-line">42 Quayside Lane<br>Harbourtown, HT4 2QL</div>
    <div class="contact-line accent"><svg width="7" height="7" viewBox="0 0 10 10"><path d="M2 0l2 2-1 2 3 3 2-1 2 2-2 2C4 10 0 6 0 2z" fill="#e8b420"/></svg>1-800-555-0193</div>
    <div class="contact-line accent"><svg width="8" height="6" viewBox="0 0 10 7"><rect width="10" height="7" fill="#e8b420"/><path d="M0 0l5 4 5-4" stroke="#161616" fill="none"/></svg>hello@tinkerharbour.example</div>
  </div>
</footer>
<div class="stripe" style="top:1056px"></div>
<div class="abs map" role="img" aria-label="Street map showing the onsite location"></div>
</body>
</html>
```